Business Card for Brevel Coatings

We need a simple, yet out standing business card for our painting company.

Target Market(s)

wealthy; high-end neighborhoods, and businesses

Industry/Entity Type

Painting

Contact Information for Business Card

Name:
Doran Vask

Email:
d.vask@brevel-coatings.com

Website:
Brevel-coatings.com

Phone Number:
(555) 416-9073

Font styles to use
Serif
Sans Serif

Requirements
Must have
• slogan "making change simple"
Should not have
• A title attached to the name on the card

```html
<!DOCTYPE html>
<html lang="en">
<head>
<meta charset="UTF-8">
<title>Brevel Coatings – Business Card</title>
<link rel="stylesheet" href="https://fonts.googleapis.com/css2?family=Arimo:wght@400;700&display=swap">
<style>
  :root {
    --forest: #3c5427;
    --lime: #b5cf3a;
    --ink: #111111;
    --paper: #ffffff;
    --backdrop: #e9e9e6;
    --rule: #7f8f6a;
  }
  * { margin: 0; padding: 0; box-sizing: border-box; }
  html, body {
    width: 1200px;
    height: 800px;
    overflow: hidden;
    background: var(--backdrop);
    font-family: "Arimo", Arial, sans-serif;
  }
  .sheet {
    position: relative;
    width: 1200px;
    height: 800px;
    display: flex;
    flex-direction: column;
    align-items: center;
    justify-content: center;
    gap: 40px;
  }
  .card {
    position: relative;
    width: 560px;
    height: 320px;
    border-radius: 22px;
    overflow: hidden;
    box-shadow: 0 6px 18px rgba(0,0,0,0.18);
  }

  /* Back side */
  .card-back {
    background: var(--forest);
    display: flex;
    flex-direction: column;
    align-items: center;
    justify-content: center;
    gap: 14px;
  }
  .brand-name {
    font-weight: 700;
    letter-spacing: 0.04em;
    white-space: nowrap;
  }
  .card-back .brand-name {
    color: var(--paper);
    font-size: 40px;
    display: flex;
    align-items: center;
    gap: 16px;
  }
  .brand-mark {
    display: inline-block;
    width: 22px;
    height: 22px;
    background: var(--paper);
  }
  .slogan {
    color: var(--paper);
    font-size: 14px;
    font-weight: 400;
    letter-spacing: 0.4em;
    text-transform: uppercase;
    padding-left: 38px;
  }

  /* Front side */
  .card-front { background: var(--paper); }
  .front-brand {
    position: absolute;
    left: 40px;
    top: 104px;
    width: 190px;
    color: var(--forest);
    font-size: 28px;
    line-height: 1.15;
    white-space: normal;
  }
  .front-slogan {
    position: absolute;
    left: 40px;
    top: 180px;
    width: 190px;
    color: var(--forest);
    font-size: 11px;
    letter-spacing: 0.18em;
    text-transform: uppercase;
  }
  .divider {
    position: absolute;
    left: 250px;
    top: 62px;
    width: 1px;
    height: 160px;
    background: linear-gradient(to bottom, rgba(127,143,106,0), var(--rule) 30%, var(--rule) 70%, rgba(127,143,106,0));
  }
  .contact {
    position: absolute;
    left: 272px;
    top: 66px;
  }
  .person-name {
    color: var(--forest);
    font-size: 24px;
    font-weight: 700;
    margin-bottom: 30px;
  }
  .contact-line {
    font-size: 18px;
    font-weight: 700;
    color: var(--ink);
    line-height: 1.3;
  }
  .contact-line.web { color: var(--forest); }
  .band {
    position: absolute;
    left: 0;
    bottom: 0;
    width: 100%;
    height: 34px;
    display: flex;
  }
  .band-dark { width: 42%; background: var(--forest); }
  .band-light { flex: 1; background: var(--lime); }
</style>
</head>
<body>
  <main class="sheet">
    <section class="card card-back" aria-label="Card back">
      <div class="brand-name"><span class="brand-mark"></span>Brevel Coatings</div>
      <p class="slogan">making change simple</p>
    </section>

    <section class="card card-front" aria-label="Card front">
      <div class="brand-name front-brand">Brevel Coatings</div>
      <p class="front-slogan">making change simple</p>
      <div class="divider"></div>
      <div class="contact">
        <p class="person-name">Doran Vask</p>
        <p class="contact-line">d.vask@brevel-coatings.com</p>
        <p class="contact-line">(555) 416-9073</p>
        <p class="contact-line web">Brevel-coatings.com</p>
      </div>
      <div class="band">
        <div class="band-dark"></div>
        <div class="band-light"></div>
      </div>
    </section>
  </main>
</body>
</html>
```